Need a Zine cover designed

I’m looking for someone who can design an eye catching and original zine cover. Incorporating the logo I included below. I’m not 100% sure which logo I want to use on the cover, if it’s possible to see how you incorporate the logos on a sample will make it easier for me to decide. Thank you for your time.
For the second logo I’m unsure how to remove the grey background, but I do not want it included in the zine cover
The title of the zine is:
Velvet Orchard
perspectives of culture, life, & love

```html
<!DOCTYPE html>
<html lang="en">
<head>
<meta charset="UTF-8">
<title>Velvet Orchard — Zine Cover</title>
<link rel="stylesheet" href="https://fonts.googleapis.com/css2?family=Anton&family=Jost:wght@400;500;600&display=swap">
<style>
  :root {
    --page: #ffffff;
    --cover: #1c1c1c;
    --orange: #ef6420;
    --blue: #12c2f0;
    --white: #ffffff;
  }
  * { margin: 0; padding: 0; box-sizing: border-box; }
  html, body {
    width: 1200px;
    height: 1200px;
    overflow: hidden;
    background: var(--page);
  }
  .canvas {
    position: relative;
    width: 1200px;
    height: 1200px;
    background: var(--page);
  }
  .cover {
    position: absolute;
    left: 289px;
    top: 120px;
    width: 621px;
    height: 960px;
    background: var(--cover);
    color: var(--white);
    font-family: "Jost", sans-serif;
  }
  .club-name {
    position: absolute;
    top: 92px;
    left: 0;
    width: 100%;
    text-align: center;
    font-family: "Jost", sans-serif;
    font-weight: 600;
    font-size: 34px;
    line-height: 1.05;
    color: var(--orange);
    letter-spacing: 0.02em;
  }
  .title {
    position: absolute;
    left: 0;
    width: 100%;
    text-align: center;
    font-family: "Anton", sans-serif;
    text-transform: uppercase;
    line-height: 1;
  }
  .title-word {
    position: relative;
    display: inline-block;
  }
  .title-word .echo {
    position: absolute;
    left: 0;
    top: 100%;
    width: 100%;
    transform-origin: top center;
    transform: scaleY(-0.42) translateY(14%);
    filter: blur(0.4px);
  }
  .title-primary {
    top: 360px;
    font-size: 112px;
    letter-spacing: 0.04em;
    color: var(--orange);
  }
  .title-secondary {
    top: 500px;
    font-size: 86px;
    letter-spacing: 0.06em;
    color: var(--blue);
  }
  .tagline {
    position: absolute;
    top: 608px;
    left: 0;
    width: 100%;
    text-align: center;
    font-size: 17px;
    font-weight: 400;
    letter-spacing: 0.12em;
    text-transform: uppercase;
  }
  .creator {
    position: absolute;
    top: 915px;
    left: 0;
    width: 100%;
    text-align: center;
    font-size: 16px;
    font-weight: 500;
    letter-spacing: 0.12em;
    text-transform: uppercase;
  }
</style>
</head>
<body>
  <main class="canvas">
    <section class="cover">
      <div class="club-name">Mellow Harbor<br>Club</div>

      <h1 class="title title-primary">
        <span class="title-word">Velvet<span class="echo" aria-hidden="true">Velvet</span></span>
      </h1>
      <h2 class="title title-secondary">
        <span class="title-word">Orchard<span class="echo" aria-hidden="true">Orchard</span></span>
      </h2>

      <p class="tagline">Perspectives of culture, life, &amp; love</p>

      <p class="creator">*** Zine creator’s name ***</p>
    </section>
  </main>
</body>
</html>
```